Business Card Design Project

We are looking to redesign the logo, business card and stationary of one of our group companies - KORVAL SUPPLY COMPANY LLC.

The company specialises in industrial PVC and CPVC Piping systems. It is situated in the Middle East and the focus is purely in this region.

The logo work is already completed. The file is uploaded for the reference.

We are looking for a clean minimalistic design for the business card.

regards
Tarun
Updates

Hello Everyone!

Thanks for submitting your designs. 

Yet to find the right design. Probably the below links will give you guys some more idea on what we would like.

Minimalist design with some creativity.

Tarun

http://layoutjournal.example/inspiration/15-beautifully-minimal-business-cards

http://www.pixelfoundry.example/2011/11/14/30-minimalist-business-card-design/

http://www.gridcrafter.example/inspiration/minimal-business-cards/

Target Market(s)

Industrial users

Industry/Entity Type

Industrial

Requirements
Must have
• - Minimalistic design

- Back side of the card should include the manufacturer PIPEMARK NORDIA's decal. The file is upload for the reference

- Further information
Company Name:
KORVAL SUPPLY COMPANY LLC
Address:
PO Box 8152, Sharjah Industrial Area 5, Qarwen Road
Sharjah, United Arab Emirates
Telephone:
+971-6-5180-392
Fax:
+977-6-5180-393
Email:
mail@ksc-holdings.example

- FYI, Korval Supply Company LLC is the authorised distributor for PIPEMARK NORDIA in the UAE. For further information on pipemark please visit the website www.pipemark-nordia.example

```html
<!DOCTYPE html>
<html lang="en">
<head>
<meta charset="utf-8">
<title>Korval Supply Company LLC — Business Card</title>
<link rel="stylesheet" href="https://fonts.googleapis.com/css2?family=Didact+Gothic&family=Montserrat:wght@700&display=swap">
<style>
  :root {
    --page-bg: #e9e7e3;
    --card-dark: #262626;
    --band-dark: #2b2b2b;
    --band-mid: #8a8a8a;
    --band-light: #d9d9d9;
    --text-light: #f2f2f2;
    --text-muted: #cfcfcf;
    --text-on-light: #6e6e6e;
    --accent-blue: #8fb4e3;
    --link-blue: #7aa7de;
    --divider: #a9a9a9;
  }
  * { box-sizing: border-box; margin: 0; padding: 0; }
  html, body { width: 1200px; height: 900px; overflow: hidden; }
  body {
    background: var(--page-bg);
    font-family: "Didact Gothic", "Century Gothic", sans-serif;
    display: flex;
    align-items: center;
    justify-content: center;
    gap: 40px;
  }
  .card {
    width: 540px;
    height: 309px;
    position: relative;
    overflow: hidden;
    box-shadow: 0 6px 18px rgba(0,0,0,.18);
  }

  /* Back side — service list */
  .card-back { background: var(--band-light); }
  .service-grid {
    display: grid;
    grid-template-columns: 1fr 1fr;
    grid-template-rows: 62px repeat(6, 1fr);
    height: 100%;
  }
  .service-row {
    display: flex;
    align-items: center;
    justify-content: center;
    font-size: 22px;
    letter-spacing: .08em;
    text-transform: uppercase;
  }
  .service-row.is-header { background: var(--band-dark); color: var(--text-light); font-size: 20px; align-items: flex-end; padding-bottom: 8px; }
  .service-row.is-mid { background: var(--band-mid); color: var(--text-light); }
  .service-row.is-light { background: var(--band-light); color: var(--text-on-light); }
  .service-row.col-left { border-right: 1px solid var(--divider); }

  /* Front side — identity */
  .card-front { background: var(--card-dark); color: var(--text-light); }
  .company-name {
    position: absolute;
    top: 44px;
    right: 34px;
    font-family: "Montserrat", "Century Gothic", sans-serif;
    font-weight: 700;
    font-size: 21px;
    letter-spacing: .02em;
  }
  .contact-block {
    position: absolute;
    top: 98px;
    right: 34px;
    text-align: right;
    font-size: 13px;
    line-height: 1.45;
    color: var(--text-muted);
  }
  .contact-block address { font-style: normal; margin-bottom: 8px; }
  .contact-line { display: flex; justify-content: flex-end; align-items: center; gap: 6px; }
  .contact-line svg { width: 11px; height: 11px; fill: var(--text-muted); }
  .contact-group { margin-bottom: 8px; }
  .contact-line.is-web { color: var(--link-blue); }
  .contact-line.is-web svg { fill: var(--link-blue); }

  .accent-bar {
    position: absolute;
    left: 0;
    bottom: 18px;
    width: 11px;
    height: 92px;
    background: var(--accent-blue);
  }
  .brand-mark {
    position: absolute;
    left: 34px;
    bottom: 40px;
    display: flex;
    align-items: center;
    gap: 10px;
  }
  .brand-square { width: 22px; height: 22px; background: var(--accent-blue); }
  .brand-name { font-size: 20px; letter-spacing: .12em; color: var(--text-light); }
</style>
</head>
<body>

  <section class="card card-back" aria-label="Business card back">
    <div class="service-grid">
      <div class="service-row is-header col-left">Community</div>
      <div class="service-row is-header">Design</div>

      <div class="service-row is-mid col-left">Pipes</div>
      <div class="service-row is-mid">Logistics</div>

      <div class="service-row is-light col-left">Fittings</div>
      <div class="service-row is-light">Finance</div>

      <div class="service-row is-mid col-left">Valves</div>
      <div class="service-row is-mid">Software</div>

      <div class="service-row is-light col-left">Accessories</div>
      <div class="service-row is-light">Infrastructure</div>

      <div class="service-row is-mid col-left">Engineering</div>
      <div class="service-row is-mid">Service</div>

      <div class="service-row is-light col-left">Training</div>
      <div class="service-row is-light">Support</div>
    </div>
  </section>

  <section class="card card-front" aria-label="Business card front">
    <h1 class="company-name">KORVAL SUPPLY COMPANY LLC</h1>

    <div class="contact-block">
      <address>
        PO Box 8152, Sharjah Industrial<br>
        Area 5, Qarwen Road<br>
        Sharjah, United Arab Emirates
      </address>
      <div class="contact-group">
        <div class="contact-line">
          <svg viewBox="0 0 24 24" aria-hidden="true"><path d="M6.6 10.8a15.1 15.1 0 0 0 6.6 6.6l2.2-2.2a1 1 0 0 1 1-.25 11.4 11.4 0 0 0 3.6.57 1 1 0 0 1 1 1V20a1 1 0 0 1-1 1A17 17 0 0 1 3 4a1 1 0 0 1 1-1h3.5a1 1 0 0 1 1 1c0 1.25.2 2.45.57 3.57a1 1 0 0 1-.25 1z"/></svg>
          <span>+971-6-5180-392</span>
        </div>
        <div class="contact-line">
          <svg viewBox="0 0 24 24" aria-hidden="true"><path d="M6 2h9l3 3v4h1a3 3 0 0 1 3 3v7h-4v3H6v-3H2v-7a3 3 0 0 1 3-3h1zm2 2v5h8V6h-2V4zm0 12v4h8v-4z"/></svg>
          <span>+977-6-5180-393</span>
        </div>
      </div>
      <div class="contact-line">
        <svg viewBox="0 0 24 24" aria-hidden="true"><path d="M2 5h20v14H2zm2 2v.5l8 5 8-5V7zm0 2.9V17h16V9.9l-8 5z"/></svg>
        <span>mail@ksc-holdings.example</span>
      </div>
      <div class="contact-line is-web">
        <svg viewBox="0 0 24 24" aria-hidden="true"><path d="M12 2a10 10 0 1 0 0 20 10 10 0 0 0 0-20zm6.9 6h-2.9a15 15 0 0 0-1.4-3.6A8 8 0 0 1 18.9 8zM12 4c.8 1.1 1.5 2.5 1.9 4h-3.8c.4-1.5 1.1-2.9 1.9-4zM4.3 14a8 8 0 0 1 0-4h3.4a16 16 0 0 0 0 4zm.8 2h2.9c.3 1.3.8 2.5 1.4 3.6A8 8 0 0 1 5.1 16zM8 8H5.1a8 8 0 0 1 4.3-3.6C8.8 5.5 8.3 6.7 8 8zm4 12c-.8-1.1-1.5-2.5-1.9-4h3.8c-.4 1.5-1.1 2.9-1.9 4zm2.3-6H9.7a14 14 0 0 1 0-4h4.6a14 14 0 0 1 0 4zm.3 5.6c.6-1.1 1.1-2.3 1.4-3.6h2.9a8 8 0 0 1-4.3 3.6zm1.7-5.6a16 16 0 0 0 0-4h3.4a8 8 0 0 1 0 4z"/></svg>
        <span>www.pipemark-nordia.example</span>
      </div>
    </div>

    <div class="accent-bar"></div>
    <div class="brand-mark">
      <span class="brand-square" aria-hidden="true"></span>
      <span class="brand-name">KORVAL</span>
    </div>
  </section>

</body>
</html>
```